Business card for a "family office" company

Please provide professional looking business card designs, incorporating the attached logo and below details. Harrowmere Holdings Pty Ltd is a family office / financial investment company. We are looking for a modern, professional and contemporary card design.

Industry/Entity Type

Finance

Contact Information for Business Card

Name: Dean Mollick
Title: Director
Company: Harrowmere Holdings Pty Ltd
Email: harrowdean@quillnet.example
Mobile: 0462 735 418
Address: 4/312 Barnaby Parade, Kestrel Bay WA 6199, Australia

Requirements
Must have
• All details above and the logo. logo only on back side. incorporate colours of logo
Nice to have
• up to you
Should not have
• ?

```html
<!DOCTYPE html>
<html lang="en">
<head>
<meta charset="utf-8">
<title>Harrowmere Holdings – Business Card</title>
<link rel="stylesheet" href="https://fonts.googleapis.com/css2?family=Open+Sans:wght@300;400;700&display=swap">
<style>
  :root {
    --page-bg: #e9e6e1;
    --card-dark: #303032;
    --card-dark-mark: #1c1c1e;
    --card-light: #ffffff;
    --navy: #3b3a78;
    --ink: #1f1f24;
    --ink-soft: #4a4a52;
    --shadow: 0 14px 30px rgba(0,0,0,0.22);
  }
  * { box-sizing: border-box; margin: 0; padding: 0; }
  html, body { width: 1200px; height: 800px; overflow: hidden; }
  body {
    background: var(--page-bg);
    font-family: "Open Sans", Arial, sans-serif;
    display: flex;
    align-items: center;
    justify-content: center;
    gap: 40px;
  }
  .card {
    width: 540px;
    height: 310px;
    border-radius: 22px;
    box-shadow: var(--shadow);
    position: relative;
    overflow: hidden;
  }
  .card--front {
    background: var(--card-dark);
    display: flex;
    align-items: center;
    justify-content: center;
  }
  .brand {
    display: flex;
    align-items: center;
    gap: 14px;
    font-weight: 400;
    text-transform: uppercase;
    letter-spacing: 0.18em;
  }
  .brand__square { width: 28px; height: 28px; flex: none; }
  .brand__name { line-height: 1.25; }
  .card--front .brand { color: var(--card-dark-mark); font-size: 22px; }
  .card--front .brand__square { background: var(--card-dark-mark); width: 40px; height: 40px; }

  .card--back { background: var(--card-light); }
  .card--back .brand {
    position: absolute;
    top: 34px;
    right: 34px;
    color: var(--navy);
    font-size: 14px;
  }
  .card--back .brand__square { background: var(--navy); }

  .person {
    position: absolute;
    left: 0;
    top: 118px;
    padding-left: 34px;
  }
  .person::before {
    content: "";
    position: absolute;
    left: 22px;
    top: 4px;
    width: 5px;
    height: 44px;
    background: var(--navy);
  }
  .person__name { font-size: 24px; color: var(--ink); line-height: 1.1; }
  .person__first { font-weight: 300; }
  .person__last { font-weight: 700; }
  .person__title { font-size: 14px; color: var(--ink-soft); margin-top: 2px; }

  .contacts {
    position: absolute;
    left: 34px;
    bottom: 30px;
    list-style: none;
    font-size: 12.5px;
    color: var(--ink-soft);
    line-height: 1.55;
  }
  .contacts__item { display: flex; align-items: flex-start; gap: 10px; }
  .contacts__icon { width: 12px; height: 12px; flex: none; margin-top: 4px; fill: var(--navy); }
  .contacts__icon .flap { fill: none; stroke: var(--card-light); stroke-width: 1.2; }
</style>
</head>
<body>
  <section class="card card--front" aria-label="Card front">
    <div class="brand">
      <span class="brand__square"></span>
      <span class="brand__name">Harrowmere<br>Holdings</span>
    </div>
  </section>

  <section class="card card--back" aria-label="Card back">
    <div class="brand">
      <span class="brand__square"></span>
      <span class="brand__name">Harrowmere<br>Holdings</span>
    </div>

    <div class="person">
      <p class="person__name"><span class="person__first">Dean</span> <span class="person__last">Mollick</span></p>
      <p class="person__title">Director</p>
    </div>

    <ul class="contacts">
      <li class="contacts__item">
        <svg class="contacts__icon" viewBox="0 0 12 12" aria-hidden="true"><rect x="0" y="2" width="12" height="8" rx="1"/><path class="flap" d="M0.5 2.5l5.5 4 5.5-4"/></svg>
        <span>harrowdean@quillnet.example</span>
      </li>
      <li class="contacts__item">
        <svg class="contacts__icon" viewBox="0 0 12 12" aria-hidden="true"><path d="M3 0h6a1 1 0 0 1 1 1v10a1 1 0 0 1-1 1H3a1 1 0 0 1-1-1V1a1 1 0 0 1 1-1zm0 2v7h6V2z"/></svg>
        <span>0462 735 418</span>
      </li>
      <li class="contacts__item">
        <svg class="contacts__icon" viewBox="0 0 12 12" aria-hidden="true"><path d="M6 0a4 4 0 0 1 4 4c0 3-4 8-4 8S2 7 2 4a4 4 0 0 1 4-4zm0 2.5a1.5 1.5 0 1 0 0 3 1.5 1.5 0 0 0 0-3z"/></svg>
        <span>4/312 Barnaby Parade<br>Kestrel Bay WA 6199, Australia</span>
      </li>
    </ul>
  </section>
</body>
</html>
```